Design for Glimmora Ad to promote Laptops purchase

Need a graphic design for a Glimmora Ad - to promote 2 laptops (PC and Vantrel) with the stated required ad-text.

AD TEXT:

FOR SME BUSINESS ONLY!
Chat with us!
To get advice on how to apply
and defray up to 80%* of business laptop purchase cost!

*Terms and Conditions apply

Image for reference only

Target Market(s)

Small medium business

Font styles to use
Sans Serif

Requirements
Must have
• 2 laptop images (see attached ) - 1 vector image of VANTREL , and pls try to create another vector image of PC laptop (where screen is showing Blue Quorvex screen)

```html
<!DOCTYPE html>
<html lang="en">
<head>
<meta charset="utf-8">
<title>Glimmora – SME Business Laptop Ad</title>
<link rel="stylesheet" href="https://fonts.googleapis.com/css2?family=Mukta:wght@400;500;700;800&display=swap">
<style>
  :root {
    --stage: #6b6b6b;
    --light-bg: #ffffff;
    --dark-bg: #333333;
    --ink-light: #111111;
    --ink-dark: #ffffff;
    --accent-light: #d42a2a;
    --accent-dark: #e04a4a;
    --chat-dot: #2f7bf0;
    --vantrel-a: #f3a6e6;
    --vantrel-b: #9a3fc4;
    --vantrel-c: #3a2a78;
    --quorvex-a: #8fd0ff;
    --quorvex-b: #1a6fd8;
    --quorvex-c: #0b2d6b;
    --shell: #cfcfcf;
  }
  * { margin: 0; padding: 0; box-sizing: border-box; }
  html, body {
    width: 982px; height: 1200px; overflow: hidden;
    background: var(--stage);
    font-family: "Mukta", sans-serif;
  }
  .canvas { position: relative; width: 982px; height: 1200px; }

  .banner {
    position: absolute; left: 87px; width: 808px; height: 423px;
    background: var(--light-bg); color: var(--ink-light);
    --accent: var(--accent-light);
  }
  .banner--light { top: 112px; }
  .banner--dark {
    top: 677px; height: 420px;
    background: var(--dark-bg); color: var(--ink-dark);
    --accent: var(--accent-dark);
  }

  .laptop {
    position: absolute; border-radius: 10px 10px 16px 16px;
  }
  .laptop--vantrel {
    left: 63px; top: 35px; width: 330px; height: 169px;
    background:
      linear-gradient(180deg, transparent 84%, var(--shell) 84%),
      radial-gradient(ellipse at 45% 40%, var(--vantrel-a) 0%, var(--vantrel-b) 45%, var(--vantrel-c) 85%);
  }
  .laptop--quorvex {
    left: 455px; top: 36px; width: 290px; height: 171px;
    background:
      linear-gradient(180deg, transparent 84%, var(--shell) 84%),
      radial-gradient(ellipse at 65% 40%, var(--quorvex-a) 0%, var(--quorvex-b) 40%, var(--quorvex-c) 85%);
  }

  .copy { position: absolute; left: 0; right: 0; text-align: center; white-space: nowrap; }
  .headline { top: 218px; font-size: 46px; font-weight: 700; line-height: 1; letter-spacing: 0.2px; }
  .chat { top: 279px; font-size: 25px; font-weight: 500; line-height: 1; display: flex; justify-content: center; align-items: center; gap: 8px; }
  .chat strong { font-weight: 800; }
  .chat-dot { width: 22px; height: 22px; border-radius: 50%; background: var(--chat-dot); }
  .advice { top: 316px; font-size: 20px; font-weight: 400; line-height: 1; }
  .offer { top: 343px; font-size: 21px; font-weight: 400; line-height: 1; color: var(--accent); }
  .offer strong { font-weight: 700; }
  .terms { position: absolute; left: 63px; top: 381px; font-size: 14px; font-weight: 400; line-height: 1; }
</style>
</head>
<body>
<main class="canvas">

  <section class="banner banner--light">
    <div class="laptop laptop--vantrel" role="img" aria-label="Vantrel laptop with purple-pink galaxy wallpaper"></div>
    <div class="laptop laptop--quorvex" role="img" aria-label="PC laptop showing the blue Quorvex start screen"></div>
    <h1 class="copy headline">Sme Business Only!</h1>
    <p class="copy chat"><span class="chat-dot"></span><span>Glimmora</span><span><strong>Chat</strong> with us!</span></p>
    <p class="copy advice">To get advice on how to apply</p>
    <p class="copy offer">and defray <strong>up to 80%</strong>* of business laptop purchase cost!</p>
    <p class="terms">*Terms and Conditions apply</p>
  </section>

  <section class="banner banner--dark">
    <div class="laptop laptop--vantrel" role="img" aria-label="Vantrel laptop with purple-pink galaxy wallpaper"></div>
    <div class="laptop laptop--quorvex" role="img" aria-label="PC laptop showing the blue Quorvex start screen"></div>
    <h2 class="copy headline">Sme Business Only!</h2>
    <p class="copy chat"><span class="chat-dot"></span><span>Glimmora</span><span><strong>Chat</strong> with us!</span></p>
    <p class="copy advice">To get advice on how to apply</p>
    <p class="copy offer">and defray <strong>up to 80%</strong>* of business laptop purchase cost!</p>
    <p class="terms">*Terms and Conditions apply</p>
  </section>

</main>
</body>
</html>
```